LoweniasMassage website required

We need a website for a mobile sports massage therapist in the United Kingdom. Specialising in pregnancy and postnatal massage, sports and remedial, deep tissue massage & Corprate Massage. Attached are some logos that we already have in various colours. The file named logo_white_background is what we normally use. Feel free to use the others at your discretion.

Requirements
Must have
• Service areas, Booking system.

```html
<!DOCTYPE html>
<html lang="en">
<head>
<meta charset="utf-8">
<title>Lowenia's Massage</title>
<link rel="stylesheet" href="https://fonts.googleapis.com/css2?family=Open+Sans:ital,wght@0,400;0,600;0,700;1,400&family=Kaushan+Script&display=swap">
<style>
  :root{
    --sky:#4fb0de;
    --sky-deep:#3a9bcc;
    --accent:#5cc3ee;
    --night:#222629;
    --night-soft:#2c3034;
    --ink:#151719;
    --footer-top:#2e6a93;
    --footer-bottom:#1f4866;
    --white:#ffffff;
    --muted:#cfd6dc;
  }
  *{box-sizing:border-box;margin:0;padding:0}
  html,body{width:1200px;height:2250px;overflow:hidden;background:var(--night)}
  body{font-family:"Open Sans",Arial,sans-serif;color:var(--white)}
  .canvas{position:relative;width:1200px;height:2250px;overflow:hidden;background:var(--sky)}
  .layer{position:absolute;left:0;top:0}
  .abs{position:absolute}
  .center{left:0;width:1200px;text-align:center}

  /* header */
  .site-header{position:absolute;left:0;top:0;width:1200px;height:76px;border-bottom:1px solid rgba(255,255,255,.18)}
  .phone{position:absolute;left:183px;top:26px;display:flex;align-items:center;gap:14px;font-size:12px;color:var(--white)}
  .nav-link{position:absolute;top:30px;font-size:12px;color:var(--white);text-decoration:none}
  .nav-link.is-active{color:var(--accent);font-weight:600}
  .brand{position:absolute;left:500px;top:34px;width:200px;text-align:center;font-size:20px;font-weight:600;color:var(--white);letter-spacing:.5px}
  .brand-dot{display:block;width:22px;height:22px;border-radius:50%;background:var(--accent);margin:0 auto 6px}
  .social{position:absolute;top:30px;display:flex;gap:14px}
  .social span{display:block;width:11px;height:11px;border-radius:50%;background:var(--white)}

  /* hero */
  .hero-title{top:290px;font-size:22px;font-weight:600;letter-spacing:6px;color:var(--white)}
  .hero-title em{font-style:normal;color:var(--accent)}
  .hero-sub{top:328px;font-size:12.5px;letter-spacing:4px;color:var(--white)}
  .hero-watermark{top:150px;font-size:110px;font-weight:700;color:rgba(255,255,255,.06);letter-spacing:4px}
  .btn{position:absolute;left:540px;width:120px;height:36px;line-height:36px;text-align:center;font-size:12px;font-weight:600;color:var(--white);border-radius:2px}
  .btn-blue{top:411px;background:linear-gradient(#5aaad3,#3b86b4)}
  .btn-dark{top:1104px;background:linear-gradient(#3a3d40,#16181a)}

  .van{position:absolute;left:327px;top:500px;width:546px;height:340px;border-radius:40px 60px 30px 30px;background:linear-gradient(160deg,#ffffff,#d8dde1 70%,#a9b1b7)}

  /* welcome */
  .kicker{font-size:14px;letter-spacing:4px;font-weight:600;color:var(--ink)}
  .welcome-kicker{top:897px}
  .display{font-size:48px;line-height:60px;font-variant:small-caps}
  .display .script{font-family:"Kaushan Script",cursive;font-variant:normal;margin-right:12px}
  .welcome-title{top:918px;color:var(--ink)}
  .welcome-title .script{color:var(--white)}
  .divider{position:absolute;left:576px;width:48px;height:2px;background:var(--white)}
  .intro{top:1038px;font-size:12.5px;line-height:20px;color:var(--ink)}

  /* services */
  .service{position:absolute;width:168px;text-align:center}
  .service-photo{width:168px;height:168px;border-radius:50%;border:5px solid var(--white);box-shadow:0 4px 12px rgba(0,0,0,.35)}
  .service-name{margin-top:14px;font-size:15px;color:var(--white);white-space:nowrap}

  /* testimonials */
  .testimonial-kicker{top:1547px;color:var(--white)}
  .testimonial-title{top:1566px;color:var(--white)}
  .testimonial-title .script{color:var(--accent)}
  .quote-mark{position:absolute;font-size:90px;line-height:90px;font-weight:700;color:var(--accent);font-family:Georgia,serif}
  .quote{top:1702px;left:310px;width:580px;text-align:center;font-size:12px;line-height:20px;font-style:italic;color:var(--white)}
  .quote-author{top:1756px;font-size:12px;color:var(--accent)}
  .dots{position:absolute;top:1826px;left:576px;display:flex;gap:10px;align-items:center}
  .dots span{display:block;width:5px;height:5px;border-radius:50%;background:rgba(255,255,255,.5)}
  .dots .is-current{width:8px;height:8px;background:var(--accent)}

  /* footer */
  .subscribe-title{top:2002px;font-size:18px;font-weight:600;color:var(--white)}
  .subscribe{position:absolute;left:326px;top:2044px;width:547px;height:41px;display:flex;border-radius:21px;overflow:hidden;background:var(--white)}
  .subscribe-input{flex:1;padding-left:24px;line-height:41px;font-size:10.5px;color:#777}
  .subscribe-btn{width:120px;line-height:41px;text-align:center;font-size:12px;font-weight:600;background:linear-gradient(#2b2e31,#0f1012);color:var(--white)}
  .footer-nav{position:absolute;top:2116px;left:0;width:1200px;display:flex;justify-content:center;gap:32px;font-size:11px}
  .footer-social{position:absolute;top:2150px;left:570px;display:flex;gap:14px}
  .footer-social span{display:block;width:10px;height:10px;border-radius:50%;background:var(--white)}
  .copyright{top:2190px;font-size:10px;color:var(--muted)}
</style>
</head>
<body>
<div class="canvas">

  <svg class="layer" width="1200" height="2250" viewBox="0 0 1200 2250" aria-hidden="true">
    <defs>
      <radialGradient id="skyGlow" cx="50%" cy="40%" r="70%">
        <stop offset="0" stop-color="#63c0ea"/>
        <stop offset="1" stop-color="#3e9fd0"/>
      </radialGradient>
      <linearGradient id="footerFill" x1="0" y1="0" x2="0" y2="1">
        <stop offset="0" stop-color="#2f6c95"/>
        <stop offset="1" stop-color="#1d4563"/>
      </linearGradient>
    </defs>
    <rect x="0" y="0" width="1200" height="2250" fill="url(#skyGlow)"/>
    <path d="M0 1420 Q600 1160 1200 1420 L1200 2250 L0 2250 Z" fill="var(--night)"/>
    <path d="M0 1845 Q600 2070 1200 1845 L1200 2250 L0 2250 Z" fill="url(#footerFill)"/>
  </svg>

  <div class="abs" role="img" aria-label="Dim collage of therapists giving massages to clients and a mother with her baby"
       style="left:0;top:0;width:1200px;height:625px;background:linear-gradient(90deg,#1c1c1e,#3a302b 35%,#2b2624 65%,#1e1d1e);clip-path:path('M0 0 H1200 V518 Q600 725 0 518 Z')"></div>

  <div class="abs" role="img" aria-label="Dim photo of candles, orchids and rolled towels in a spa"
       style="left:0;top:1420px;width:1200px;height:530px;background:linear-gradient(90deg,#1d2023,#2f2b28 30%,#262829 70%,#1c1f22);clip-path:path('M0 0 Q600 -260 1200 0 V425 Q600 650 0 425 Z')"></div>

  <header class="site-header">
    <div class="phone">
      <svg width="20" height="20" viewBox="0 0 24 24" aria-hidden="true"><path d="M6.6 10.8a15.1 15.1 0 0 0 6.6 6.6l2.2-2.2a1 1 0 0 1 1-.25 11.4 11.4 0 0 0 3.6.57 1 1 0 0 1 1 1V20a1 1 0 0 1-1 1A17 17 0 0 1 3 4a1 1 0 0 1 1-1h3.5a1 1 0 0 1 1 1c0 1.25.2 2.45.57 3.57a1 1 0 0 1-.25 1z" fill="var(--accent)"/></svg>
      <span>123 456 7890</span>
    </div>
    <a class="nav-link is-active" style="left:352px">Home</a>
    <a class="nav-link" style="left:420px">About Us</a>
    <div class="brand"><span class="brand-dot"></span>Lowenia's Massage</div>
    <a class="nav-link" style="left:730px">Services</a>
    <a class="nav-link" style="left:807px">Contact Us</a>
    <div class="social" style="left:952px" aria-label="Social links"><span></span><span></span><span></span></div>
  </header>

  <div class="abs center hero-watermark" aria-hidden="true">Lowenia's Massage</div>
  <h1 class="abs center hero-title">A MOBILE <em>SPORTS MASSAGE</em> THERAPIST</h1>
  <p class="abs center hero-sub">IN THE UNITED KINGDOM</p>
  <a class="btn btn-blue">Book Now</a>

  <div class="van" role="img" aria-label="White mobile massage van with the business name on its side"></div>

  <p class="abs center kicker welcome-kicker">WELCOME TO</p>
  <h2 class="abs center display welcome-title"><span class="script">Lowenia's</span>Massage</h2>
  <span class="divider" style="top:1010px"></span>
  <p class="abs center intro">We are a mobile sports massage therapist in the United Kingdom. Specialising in pregnancy and postnatal<br>massage, sports and remedial, deep tissue massage.</p>
  <a class="btn btn-dark">Book Now</a>

  <div class="service" style="left:195px;top:1250px">
    <div class="service-photo" role="img" aria-label="Pregnant woman lying on her side during a massage" style="background:linear-gradient(135deg,#6b5a7e,#3b3340)"></div>
    <p class="service-name">Pregnancy Massage</p>
  </div>
  <div class="service" style="left:408px;top:1216px">
    <div class="service-photo" role="img" aria-label="Mother and baby at a postnatal session" style="background:linear-gradient(135deg,#e4b9a0,#9c8f86)"></div>
    <p class="service-name">Postnatal Massage</p>
  </div>
  <div class="service" style="left:622px;top:1216px">
    <div class="service-photo" role="img" aria-label="Therapist treating an athlete's leg" style="background:linear-gradient(135deg,#8a8d90,#2d2f31)"></div>
    <p class="service-name">Sports and Remedial</p>
  </div>
  <div class="service" style="left:835px;top:1250px">
    <div class="service-photo" role="img" aria-label="Deep tissue back massage" style="background:linear-gradient(135deg,#b7773f,#4a2a17)"></div>
    <p class="service-name">Deep Tissue Massage</p>
  </div>

  <p class="abs center kicker testimonial-kicker">WHAT OUR</p>
  <h2 class="abs center display testimonial-title"><span class="script">Clients</span>Says</h2>
  <span class="divider" style="top:1660px"></span>
  <span class="quote-mark" style="left:228px;top:1680px">&#8220;</span>
  <p class="abs quote">" Lorem ipsum dolor sit amet, consectetur adipiscing elit, sed do eiusmod tempor incididunt ut labore et dolore magna aliqua. Ut enim ad minim veniam, quis nostrud exercitation ullamco laboris nisi ut commodo consequat. "</p>
  <p class="abs center quote-author">Mara Ellison</p>
  <span class="quote-mark" style="left:916px;top:1728px">&#8221;</span>
  <div class="dots"><span></span><span class="is-current"></span><span></span></div>

  <p class="abs center subscribe-title">Subscribe for Our Newsletters</p>
  <div class="subscribe">
    <span class="subscribe-input">Enter your Email Address</span>
    <span class="subscribe-btn">Subscribe</span>
  </div>
  <nav class="footer-nav"><span>Home</span><span>About Us</span><span>Services</span><span>Contact Us</span></nav>
  <div class="footer-social" aria-label="Social links"><span></span><span></span><span></span></div>
  <p class="abs center copyright">Copyright © 2018 Lowenia's Massage. All rights reserved.</p>

</div>
</body>
</html>
```